residential roofing company needs a Truck wrap design.

We need a Van wrap design. We are a local residential roofing contractor.That specialize in Roofing Eavestrough and siding we need a design that will stand out and look professional.We really want roofing to stand out as that's our main focus. We like a clean a simple and modern design. Our website is www.larkfieldexteriors.ca The van we are wrapping is a 2019 Halvorsen-Kraft Tolvane 2500 Cargo 170 WB High Roof. We want to incorporate our phone number 844 612 DECK

```html
<!DOCTYPE html>
<html lang="en">
<head>
<meta charset="utf-8">
<title>Larkfield Exteriors – Van Wrap</title>
<link rel="stylesheet" href="https://fonts.googleapis.com/css2?family=Archivo+Black&family=Krona+One&family=Montserrat:wght@600&family=Ubuntu:wght@500&display=swap">
<style>
  :root {
    --ink: #4a545b;
    --amber: #f9a825;
    --sheet: #ffffff;
    --panel: #f7f8f8;
    --body-light: #fdfdfd;
    --body-shade: #d9dddf;
    --trim: #8c999e;
  }
  * { margin: 0; padding: 0; box-sizing: border-box; }
  html, body { width: 1200px; height: 761px; overflow: hidden; background: var(--sheet); }
  .sheet { position: relative; width: 1200px; height: 761px; }

  .view { position: absolute; background: var(--panel); overflow: hidden; }
  .view--side-top { left: 0; top: 20px; width: 850px; height: 345px; }
  .view--back { left: 885px; top: 27px; width: 303px; height: 340px; }
  .view--side-bottom { left: 0; top: 392px; width: 850px; height: 344px; }
  .view--front { left: 895px; top: 392px; width: 295px; height: 330px; }

  .van-body { position: absolute;
    background: linear-gradient(180deg, var(--body-light) 0%, var(--body-light) 62%, var(--body-shade) 63%, var(--trim) 80%, var(--body-light) 81%); }
  .view--side-top .van-body { left: 12px; top: 22px; width: 826px; height: 300px; border-radius: 140px 30px 20px 30px; }
  .view--side-bottom .van-body { left: 14px; top: 20px; width: 826px; height: 300px; border-radius: 30px 140px 30px 20px; }
  .view--back .van-body { left: 28px; top: 18px; width: 248px; height: 315px; border-radius: 40px 40px 14px 14px; }
  .view--front .van-body { left: 28px; top: 12px; width: 240px; height: 310px; border-radius: 40px 40px 14px 14px; }

  .layer { position: absolute; white-space: nowrap; color: var(--ink); line-height: 1; }
  .phone { font-family: "Krona One", sans-serif; font-weight: 400; }
  .web { font-family: "Ubuntu", sans-serif; font-weight: 500; color: var(--amber); }
  .web--ink { color: var(--ink); }
  .mark { position: absolute; background: var(--amber); }

  .lockup { position: absolute; white-space: nowrap; color: var(--ink); }
  .lockup__name, .lockup__sub { display: block; font-family: "Archivo Black", sans-serif; line-height: 1; }
  .lockup__tag { display: block; font-family: "Montserrat", sans-serif; font-weight: 600; line-height: 1; letter-spacing: 0.42em; }
  .lockup--center { text-align: center; }

  .split { position: absolute; white-space: nowrap; line-height: 1; }
  .split--left { text-align: right; }
  .split--right { text-align: left; }
</style>
</head>
<body>
<main class="sheet">

  <section class="view view--side-top">
    <div class="van-body" role="img" aria-label="Side outline drawing of the high-roof cargo van, facing left"></div>
    <div class="layer phone" style="left:300px; top:34px; font-size:36px;">844 612 DECK</div>
    <div class="mark" style="left:360px; top:80px; width:74px; height:74px;"></div>
    <div class="lockup" style="left:498px; top:86px;">
      <span class="lockup__name" style="font-size:42px;">LARKFIELD</span>
      <span class="lockup__sub" style="font-size:29px; margin-top:4px;">EXTERIORS.ca</span>
      <span class="lockup__tag" style="font-size:12px; margin-top:14px;">ROOFING &amp; EXTERIORS</span>
    </div>
    <div class="mark" style="left:194px; top:190px; width:60px; height:60px;"></div>
    <div class="lockup" style="left:315px; top:194px;">
      <span class="lockup__name" style="font-size:22px;">LARKFIELD</span>
      <span class="lockup__sub" style="font-size:15px; margin-top:2px;">EXTERIORS.ca</span>
      <span class="lockup__tag" style="font-size:7px; margin-top:3px;">ROOFING &amp; EXTERIORS</span>
    </div>
    <div class="layer web" style="left:488px; top:198px; font-size:23px;">www.larkfieldexteriors.ca</div>
  </section>

  <section class="view view--back">
    <div class="van-body" role="img" aria-label="Rear outline drawing of the van with twin doors"></div>
    <div class="split split--left web web--ink" style="left:60px; top:30px; width:88px; font-size:11px;">www.larkfield</div>
    <div class="split split--right web web--ink" style="left:156px; top:30px; width:90px; font-size:11px;">exteriors.ca</div>
    <div class="split split--left phone" style="left:60px; top:48px; width:88px; font-size:12px; color:var(--ink);">844 612</div>
    <div class="split split--right phone" style="left:156px; top:48px; width:90px; font-size:12px; color:var(--ink);">DECK</div>
    <div class="mark" style="left:90px; top:86px; width:32px; height:32px;"></div>
    <div class="mark" style="left:183px; top:86px; width:32px; height:32px;"></div>
    <div class="lockup lockup--center" style="left:66px; top:126px; width:80px;">
      <span class="lockup__name" style="font-size:12px;">LARKFIELD</span>
      <span class="lockup__sub" style="font-size:8px; margin-top:1px;">EXTERIORS.ca</span>
      <span class="lockup__tag" style="font-size:4px; margin-top:2px; letter-spacing:0.3em;">ROOFING &amp; EXTERIORS</span>
    </div>
    <div class="lockup lockup--center" style="left:159px; top:126px; width:80px;">
      <span class="lockup__name" style="font-size:12px;">LARKFIELD</span>
      <span class="lockup__sub" style="font-size:8px; margin-top:1px;">EXTERIORS.ca</span>
      <span class="lockup__tag" style="font-size:4px; margin-top:2px; letter-spacing:0.3em;">ROOFING &amp; EXTERIORS</span>
    </div>
  </section>

  <section class="view view--side-bottom">
    <div class="van-body" role="img" aria-label="Side outline drawing of the high-roof cargo van, facing right"></div>
    <div class="layer phone" style="left:92px; top:34px; font-size:36px;">844 612 DECK</div>
    <div class="lockup" style="left:92px; top:86px;">
      <span class="lockup__name" style="font-size:42px;">LARKFIELD</span>
      <span class="lockup__sub" style="font-size:29px; margin-top:4px;">EXTERIORS.ca</span>
      <span class="lockup__tag" style="font-size:12px; margin-top:14px;">ROOFING &amp; EXTERIORS</span>
    </div>
    <div class="mark" style="left:418px; top:80px; width:74px; height:74px;"></div>
    <div class="layer web" style="left:76px; top:198px; font-size:23px;">www.larkfieldexteriors.ca</div>
    <div class="lockup" style="left:393px; top:194px;">
      <span class="lockup__name" style="font-size:22px;">LARKFIELD</span>
      <span class="lockup__sub" style="font-size:15px; margin-top:2px;">EXTERIORS.ca</span>
      <span class="lockup__tag" style="font-size:7px; margin-top:3px;">ROOFING &amp; EXTERIORS</span>
    </div>
    <div class="mark" style="left:597px; top:190px; width:60px; height:60px;"></div>
  </section>

  <section class="view view--front">
    <div class="van-body" role="img" aria-label="Front outline drawing of the van with windshield and grille"></div>
    <div class="lockup lockup--center" style="left:28px; top:20px; width:240px;">
      <span class="lockup__name" style="font-size:21px;">LARKFIELD</span>
      <span class="lockup__sub" style="font-size:14px; margin-top:2px;">EXTERIORS.ca</span>
      <span class="lockup__tag" style="font-size:6px; margin-top:3px;">ROOFING &amp; EXTERIORS</span>
    </div>
    <div class="mark" style="left:130px; top:148px; width:34px; height:34px;"></div>
  </section>

</main>
</body>
</html>
```